Ledgerwise Forge - WordPress Theme & Logo

Design a logo and Wordpress website design for Ledgerwise Forge. Ledgerwise Forge provides cryptocurrency development services to clients who need a team to create & continue developing a new cryptocurrency or who want to replace their current cryptocurrency development team. more details in the attached document.
Updates

Target Market(s)

Entrepreneurs who are building a business / platform that makes use of an underlying cryptocurrency.

Logo Text

LF or Ledgerwise Forge

Coding

Coded - Design and coding required

Font styles to use
Sans Serif

Requirements
Must have
• Professional logo, complete coded Wordpress theme for all pages, containing all specified links and buttons
Nice to have
• It would be nice if the buttons that are meant to integrate with Dealstream contain the necessary code for that. I can provide any necessary Dealstream details from my account.
Should not have
• Slow loading time

```html
<!DOCTYPE html>
<html lang="en">
<head>
<meta charset="utf-8">
<title>Ledgerwise Forge — Cryptocurrency Development</title>
<link rel="stylesheet" href="https://fonts.googleapis.com/css2?family=Montserrat:wght@600;700;800&family=Roboto:wght@400;500;700&display=swap">
<style>
:root{
  --brand:#0c56b0;
  --brand-dark:#0a3f8a;
  --navy:#141d52;
  --navy-deep:#0b1238;
  --ink:#1f2733;
  --muted:#6b7380;
  --pale:#eaf1fa;
  --foot:#f3f4f6;
  --white:#ffffff;
  --star:#f2c21b;
}
*{margin:0;padding:0;box-sizing:border-box}
html,body{width:1200px;height:4392px;overflow:hidden}
body{font-family:"Roboto",sans-serif;color:var(--ink);background:var(--white);position:relative}
.abs{position:absolute}
h1,h2,h3{font-family:"Montserrat",sans-serif}
.sec-title{position:absolute;left:0;width:1200px;text-align:center;font-size:27px;font-weight:700;color:var(--ink);letter-spacing:.3px}
.sec-title::after{content:"";display:block;width:124px;height:3px;background:var(--brand);margin:12px auto 0}
.btn{position:absolute;display:flex;align-items:center;justify-content:center;border-radius:26px;font-family:"Roboto",sans-serif;font-weight:700;font-size:14px;color:var(--white);background:linear-gradient(180deg,#1b6fd0,var(--brand-dark));letter-spacing:.3px}

/* header */
.site-header{top:0;left:0;width:1200px;height:82px;background:var(--white)}
.brand{display:flex;align-items:center;gap:12px}
.brand-mark{width:58px;height:58px;border-radius:50%;background:var(--brand)}
.brand-name{font-family:"Roboto",sans-serif;font-weight:700;font-size:14px;line-height:17px;color:var(--navy);text-transform:uppercase}
.nav{top:31px;left:320px;display:flex;gap:20px;font-size:15px;color:var(--ink)}
.nav .active{color:var(--brand)}

/* hero */
.hero{top:82px;left:0;width:1200px;height:668px;background:radial-gradient(circle at 78% 40%,#5c7da3 0%,#2b4466 30%,#14223a 62%,#0b1526 100%)}
.hero h1{position:absolute;left:111px;top:197px;font-size:29px;line-height:40px;font-weight:800;color:var(--white)}

/* welcome */
.welcome{top:750px;left:0;width:1200px;height:268px;background:var(--pale)}
.welcome p{position:absolute;left:200px;top:143px;width:800px;text-align:center;font-size:14.5px;line-height:25.5px;color:#4a5260}

/* about */
.about-photo{left:110px;top:1107px;width:453px;height:453px;border-radius:50%;background:var(--brand)}
.about-photo span{position:absolute;left:20px;top:8px;width:434px;height:434px;border-radius:50%;border:5px solid #fff;background:linear-gradient(135deg,#1d2b3d,#5b4a3c 55%,#2d4f78)}
.about-title{left:614px;top:1156px;font-size:34px;font-weight:800;display:flex;align-items:center;gap:16px}
.about-title::after{content:"";width:94px;height:3px;background:var(--brand)}
.about-copy{left:614px;top:1218px;width:476px;font-size:13.8px;line-height:24px;color:var(--muted);text-align:justify}
.about-copy p+p{margin-top:15px}

/* services */
.services{top:1650px;left:0;width:1200px;height:580px;background:linear-gradient(180deg,var(--navy) 0%,#162a6e 55%,#1a4d93 100%)}
.services .sec-title{color:var(--white);top:58px}
.service-card{position:absolute;top:160px;width:316px;height:353px;background:var(--white);border-radius:6px;padding:16px 15px}
.service-card h3{font-family:"Roboto",sans-serif;font-size:19px;font-weight:500;margin:14px 0 14px}
.service-card ul{list-style:none}
.service-card li{position:relative;padding-left:28px;font-size:13.5px;line-height:20px;color:#3b4350;margin-bottom:5px}
.service-card li::before{content:"";position:absolute;left:0;top:3px;width:11px;height:11px;border:2px solid var(--brand);border-radius:50%}
.card-icon{width:90px;height:90px}

/* offerings */
.offer-line{top:2505px;left:112px;width:975px;height:2px;background:linear-gradient(90deg,#6d9fdb,var(--brand),#6d9fdb)}
.offer{position:absolute;top:2400px;width:220px;margin-left:-110px;text-align:center;font-size:14.5px;color:#4a5260}
.offer-icon{width:72px;height:72px;margin:0 auto;border-radius:50%;background:var(--brand);border:5px solid #cfe0f5;display:flex;align-items:center;justify-content:center}
.offer-dot{width:24px;height:24px;margin:21px auto 0;border-radius:50%;background:var(--brand)}
.offer span{display:block;margin-top:8px}

/* why */
.why{top:2638px;left:0;width:1200px;height:512px;background:var(--pale)}
.why-card{position:absolute;top:145px;width:312px;height:304px;background:var(--white);border-radius:22px;text-align:center;padding-top:38px}
.why-card.featured{box-shadow:0 6px 22px rgba(10,40,90,.16)}
.why-card.featured::after{content:"";position:absolute;left:34px;right:34px;bottom:0;height:4px;background:var(--brand);border-radius:2px}
.why-icon{width:102px;height:102px;margin:0 auto;border-radius:50%;background:#3a3d42;display:flex;align-items:center;justify-content:center}
.why-card.featured .why-icon{background:var(--brand)}
.why-card h3{font-family:"Roboto",sans-serif;font-size:21px;font-weight:500;margin:35px 0 17px}
.why-card p{font-size:15.5px;line-height:24px;color:#3b4350;padding:0 40px}

/* testimonials */
.testi{position:absolute;top:3358px;width:316px;height:218px;background:var(--white);border-radius:10px;border-top:3px solid var(--brand);box-shadow:0 3px 12px rgba(0,0,0,.08);text-align:center;padding-top:58px}
.testi-badge{position:absolute;left:122px;top:-39px;width:72px;height:72px;border-radius:50%;background:var(--white);border:3px solid var(--brand);display:flex;align-items:center;justify-content:center;font-size:10px;font-weight:700;color:var(--brand);text-transform:uppercase}
.testi h3{font-family:"Roboto",sans-serif;font-size:19px;font-weight:500}
.stars{color:var(--star);font-size:11px;letter-spacing:3px;margin:2px 0 12px}
.testi p{font-size:13.6px;line-height:25px;color:var(--muted);padding:0 10px}

/* cta */
.cta{top:3673px;left:0;width:1200px;height:500px;background:linear-gradient(120deg,#1a2f86 0%,#1656b8 55%,#2a78d4 100%)}
.cta h2{position:absolute;top:44px;left:0;width:1200px;text-align:center;color:var(--white);font-size:27px;font-weight:700}
.cta p{position:absolute;top:116px;left:160px;width:880px;text-align:center;color:#e6eefb;font-size:14.5px;line-height:25.5px}
.btn-light{background:var(--white);color:var(--brand);border-radius:26px}

/* footer */
.foot-col h4{font-family:"Roboto",sans-serif;font-size:17px;font-weight:500;color:var(--ink)}
.foot-col h4::after{content:"";display:block;width:36px;height:2px;background:var(--brand);margin-top:6px}
.foot-col ul{list-style:none;margin-top:14px}
.foot-col li{position:relative;padding-left:31px;font-size:14.5px;color:#3b4350;height:25px}
.foot-col li::before{content:"";position:absolute;left:0;top:4px;width:11px;height:11px;border:2px solid var(--brand);border-radius:50%}
.social{top:4240px;left:142px;display:flex;gap:7px}
.social span{width:35px;height:35px;border-radius:50%;border:2px solid var(--brand-dark);display:block}
.social span:first-child{background:var(--brand-dark)}
.newsletter{top:4190px;left:779px;width:308px;height:47px;border-radius:24px;background:var(--white);border:1px solid #dfe3ea;display:flex;align-items:center;justify-content:space-between;padding:0 4px 0 17px;font-size:14px;color:#7a818c}
.newsletter b{width:39px;height:39px;border-radius:50%;background:var(--brand);display:flex;align-items:center;justify-content:center}
.rule{top:4326px;left:0;width:1200px;height:1px;background:#dfe2e7}
.copy{top:4350px;left:0;width:1200px;text-align:center;font-size:12.5px;color:#3b4350}
</style>
</head>
<body>

<header class="abs site-header">
  <div class="abs brand" style="left:111px;top:12px">
    <span class="brand-mark"></span>
    <span class="brand-name">Ledgerwise<br>Forge</span>
  </div>
  <nav class="abs nav">
    <span class="active">Home</span><span>About Us</span><span>Services</span><span>Our Methods</span><span>Testimonials</span><span>Blog</span>
  </nav>
  <a class="btn" style="left:861px;top:19px;width:226px;height:47px;font-size:14px;font-weight:500">SCHEDULE CONSULTATION</a>
</header>

<section class="abs hero" role="img" aria-label="Glowing wireframe cube over a blue network of connected nodes">
  <h1>YOUR OWN CRYPTOCURRENCY.<br>SECURE, EASY TO USE, AND<br>BUILT BY AN EXPERT TEAM.</h1>
  <a class="btn" style="left:111px;top:353px;width:213px;height:47px;font-size:13px">DOWNLOAD A FREE PDF</a>
  <svg class="abs" style="left:0;top:0" width="1200" height="668" viewBox="0 0 1200 668">
    <path d="M0,540 Q600,796 1200,540 L1200,668 L0,668 Z" fill="#eaf1fa"/>
    <path d="M0,540 Q600,796 1200,540" fill="none" stroke="#0c56b0" stroke-width="5"/>
  </svg>
</section>

<section class="abs welcome">
  <h2 class="sec-title" style="top:64px">WELCOME TO LEDGERWISE FORGE</h2>
  <p>Ledgerwise Forge adds professionalism to cryptocurrency development. Our done-for-you service covers everything from development and IT operations to ongoing support. You have access to a full team, for less than the typical cost of a single developer.</p>
</section>

<div class="abs about-photo"><span role="img" aria-label="Developer at a desk studying trading charts on a monitor"></span></div>
<h2 class="abs about-title">ABOUT ME</h2>
<div class="abs about-copy">
  <p>Ledgerwise Forge provides a complete service that handles the development, IT operations and support for your cryptocurrency. Cryptocurrency development can be difficult and complex, and a quality development team is hard to find and expensive.</p>
  <p>Ledgerwise Forge has an experienced team that has helped several clients launch and enhance their cryptocurrencies, including successfully running the Veltrix cryptocurrency since 2017, and writing a next-generation cryptocurrency from scratch.</p>
</div>
<a class="btn" style="left:614px;top:1452px;width:143px;height:48px">READ MORE</a>

<section class="abs services">
  <h2 class="sec-title">OUR SERVICES</h2>
  <article class="service-card" style="left:112px">
    <svg class="card-icon" viewBox="0 0 90 90" fill="none" stroke="#1f2733" stroke-width="2"><circle cx="45" cy="45" r="34" stroke-dasharray="6 6"/><path d="M45 28l15 8v17l-15 8-15-8V36z"/><path d="M30 36l15 8 15-8M45 44v17" stroke="#0c56b0"/></svg>
    <h3>Blockchain Creation &amp; Launch</h3>
    <ul><li>Base fixed price for cryptocurrency development &amp; launch–would be customizable based on client requirements</li></ul>
  </article>
  <article class="service-card" style="left:441px">
    <svg class="card-icon" viewBox="0 0 90 90" fill="none" stroke="#1f2733" stroke-width="2"><circle cx="45" cy="45" r="14" stroke="#0c56b0"/><path d="M31 45H12M59 45h19M45 31V12M45 59v19M35 35L20 20M55 55l15 15M55 35l15-15M35 55L20 70"/></svg>
    <h3>Basic offering</h3>
    <ul>
      <li>Lower cost per month</li>
      <li>Slower release schedule (about every 3 months)</li>
      <li>Client assists with testing new releases</li>
      <li>Less input into future roadmap/features</li>
      <li>Limited support hours/priority (always available for emergencies)</li>
    </ul>
  </article>
  <article class="service-card" style="left:770px">
    <svg class="card-icon" viewBox="0 0 90 90" fill="none" stroke="#1f2733" stroke-width="2"><rect x="18" y="10" width="38" height="70" rx="5"/><rect x="36" y="30" width="32" height="32" rx="3" stroke="#0c56b0"/><path d="M52 38l8 4v9l-8 4-8-4v-9z" stroke="#0c56b0"/></svg>
    <h3>Full service offering</h3>
    <ul>
      <li>Mid-range cost per month</li>
      <li>Releases every 1.5 - 2 months</li>
      <li>Client can help request/prioritize new features</li>
      <li>Full testing by my team prior to release</li>
      <li>Priority support during normal business hours, always available for emergencies</li>
    </ul>
  </article>
</section>

<h2 class="sec-title" style="top:2310px">OUR OFFERINGS</h2>
<div class="abs offer-line"></div>
<div class="offer" style="left:256px"><div class="offer-icon"><svg width="34" height="34" viewBox="0 0 34 34" fill="none" stroke="#fff" stroke-width="2"><path d="M17 4l12 7v12l-12 7-12-7V11z"/><path d="M5 11l12 7 12-7M17 18v12"/></svg></div><div class="offer-dot"></div><span>Blockchain Creation &amp; Launch</span></div>
<div class="offer" style="left:503px"><div class="offer-icon"><svg width="34" height="34" viewBox="0 0 34 34" fill="none" stroke="#fff" stroke-width="2"><rect x="4" y="6" width="26" height="18" rx="2"/><path d="M12 30h10M17 24v6M9 13h10M9 18h16"/></svg></div><div class="offer-dot"></div><span>Blockchain Development</span></div>
<div class="offer" style="left:736px"><div class="offer-icon"><svg width="34" height="34" viewBox="0 0 34 34" fill="none" stroke="#fff" stroke-width="2"><rect x="4" y="4" width="10" height="10"/><rect x="20" y="4" width="10" height="10"/><rect x="4" y="20" width="10" height="10"/><rect x="20" y="20" width="10" height="10"/></svg></div><div class="offer-dot"></div><span>Blockchain Operations</span></div>
<div class="offer" style="left:946px"><div class="offer-icon"><svg width="34" height="34" viewBox="0 0 34 34" fill="none" stroke="#fff" stroke-width="2"><rect x="4" y="5" width="26" height="20" rx="2"/><circle cx="17" cy="22" r="6"/><path d="M4 10h26"/></svg></div><div class="offer-dot"></div><span>Blockchain Support</span></div>

<section class="abs why">
  <h2 class="sec-title" style="top:57px">WHY CHOOSE US</h2>
  <article class="why-card" style="left:112px">
    <div class="why-icon"><svg width="52" height="52" viewBox="0 0 52 52" fill="none" stroke="#fff" stroke-width="2"><path d="M18 10h16l6 7-14 14-14-14z"/><path d="M4 38c6-4 12-4 18 0h10c3 0 3 4 0 4H20M22 42l18-4c4-1 6 2 3 4L30 48H12"/></svg></div>
    <h3>VALUE</h3>
    <p>A team of experts, regular updates, and fixed costs</p>
  </article>
  <article class="why-card featured" style="left:443px">
    <div class="why-icon"><svg width="52" height="52" viewBox="0 0 52 52" fill="none" stroke="#fff" stroke-width="2"><circle cx="26" cy="20" r="9"/><path d="M14 20a12 12 0 0124 0M10 46c2-9 8-13 16-13s14 4 16 13"/></svg></div>
    <h3>SUPPORT</h3>
    <p>Receive advice and other services, beyond development.</p>
  </article>
  <article class="why-card" style="left:776px">
    <div class="why-icon"><svg width="52" height="52" viewBox="0 0 52 52" fill="none" stroke="#fff" stroke-width="2"><rect x="13" y="6" width="26" height="38" rx="2"/><path d="M19 14h14M19 20h14"/><circle cx="26" cy="30" r="5"/><path d="M23 35v9l3-2 3 2v-9"/></svg></div>
    <h3>COMMITMENT</h3>
    <p>Enjoy regular updates and new features.</p>
  </article>
</section>

<h2 class="sec-title" style="top:3233px">CLIENT TESTIMONIALS</h2>
<article class="testi" style="left:112px"><div class="testi-badge">Cadenza</div><h3>Lorum Ipsum Dolor</h3><div class="stars">★★★★★</div><p>Lorem ipsum dolor sit amet, consectetur adip iscing elit, sed do eiusmod tempor incididu ntut labore et dolore magna aliquaudet enimad minim veniam quis.</p></article>
<article class="testi" style="left:441px"><div class="testi-badge">Norvale</div><h3>Lorum Ipsum Dolor</h3><div class="stars">★★★★★</div><p>Lorem ipsum dolor sit amet, consectetur adip iscing elit, sed do eiusmod tempor incididu ntut labore et dolore magna aliquaudet enimad minim veniam quis.</p></article>
<article class="testi" style="left:770px"><div class="testi-badge">Corvane</div><h3>Lorum Ipsum Dolor</h3><div class="stars">★★★★★</div><p>Lorem ipsum dolor sit amet, consectetur adip iscing elit, sed do eiusmod tempor incididu ntut labore et dolore magna aliquaudet enimad minim veniam quis.</p></article>

<section class="abs cta">
  <h2>SCHEDULE A FREE CONSULTATION</h2>
  <p>Lorem ipsum dolor sit amet, consectetur adipiscing elit, sed do eiusmod tempor incididunt ut labore et dolore magna aliqua. Ut enim ad minim veniam, quis nostrud exercitation ullamco laboris nisi ut aliquip ex ea commodo consequat. Duis aute irure dolor in reprehenderit in voluptate velit esse cillum dolore eu fugiat nulla pariatur excepteur.</p>
  <a class="btn btn-light" style="left:528px;top:220px;width:144px;height:48px">GET STARTED</a>
</section>
<svg class="abs" style="left:0;top:3950px" width="1200" height="442" viewBox="0 0 1200 442">
  <path d="M0,190 Q600,20 1200,190 L1200,442 L0,442 Z" fill="#f3f4f6"/>
</svg>

<div class="abs brand" style="left:112px;top:4146px">
  <span class="brand-mark" style="width:62px;height:62px"></span>
  <span class="brand-name" style="font-size:16px;line-height:19px">Ledgerwise<br>Forge</span>
</div>
<div class="abs social"><span></span><span></span><span></span><span></span></div>

<div class="abs foot-col" style="left:383px;top:4142px"><h4>Quick Links</h4><ul><li>Home</li><li>About Us</li><li>Our Services</li><li>Our Methods</li><li>Contact Us</li></ul></div>
<div class="abs foot-col" style="left:552px;top:4142px"><h4>About Links</h4><ul><li>Blog</li><li>Search</li><li>Privacy Policy</li><li>Terms Of Conditions</li></ul></div>
<div class="abs foot-col" style="left:779px;top:4142px"><h4>Get Our Newsletter</h4></div>
<div class="abs newsletter">Enter Email Address<b><svg width="18" height="18" viewBox="0 0 18 18"><path d="M2 9L16 2 12 16 9 10z" fill="#fff"/></svg></b></div>

<div class="abs rule"></div>
<div class="abs copy">Copyrights 2021 LEDGERWISE FORGE. All Rights Reserved</div>

</body>
</html>
```